Pravo Vet Core Values

Pravo Veterinary Services is both a small and large animal practice so we mainly work with cats, dogs, and cows. We want the sign to reflect all three of those animals as well as elements of farm/country life like barns and tractors. We're located in a small town, less then 4,000 people, so we would like the design to have a rural look and feel. We want to use a "rustic" color palette, follow the link to see what we have in mind https://www.tolbrek-paints.example/homeowners/color/find-and-explore-colors/paint-colors-by-collection/lifestyle-collection/mossy-loam.
The text we want have appear on the sign is listed below. We also want to C in compassionate, the A in Always, the R in Ready, the E in Expanding, and the S in Service to be bold and standout since they will spell out cares.
"Pravo Veterinary Services is committed to Compassionate and honest care for all patients and clients. This means we are Always efficient with our resources to pass the savings on to our clients. We are also Ready to help with the best medicine available while Expanding to help more of our practice’s families and farms. This is how we provide Service in abundance to all our clients so they are proud to send their family and friends to see us. Pravo Vet CARES."

```html
<!DOCTYPE html>
<html lang="en">
<head>
<meta charset="utf-8">
<title>Pravo Vet Core Values</title>
<link rel="stylesheet" href="https://fonts.googleapis.com/css2?family=Graduate&family=Alfa+Slab+One&family=Audiowide&family=Almendra:wght@700&family=Fondamento&family=Michroma&family=Racing+Sans+One&family=Russo+One&family=Exo+2:ital,wght@0,400;0,800;1,300;1,900&family=Rye&family=Skranji:wght@700&family=Bungee+Hairline&family=Oswald:wght@600&display=swap">
<style>
  :root {
    --paper: #ececec;
    --pattern: #e2e3e2;
    --forest: #2b6a3b;
    --pine: #1f5a30;
    --fern: #3f8f4e;
    --sage: #6aa172;
    --mint: #4fd89b;
  }
  * { margin: 0; padding: 0; box-sizing: border-box; }
  html, body { width: 921px; height: 1200px; overflow: hidden; background: var(--paper); }
  .sign { position: relative; width: 921px; height: 1200px; background: var(--paper); color: var(--forest); }
  .pattern { position: absolute; inset: 0; background: linear-gradient(180deg, var(--paper), var(--pattern) 50%, var(--paper)); }
  .line { position: absolute; left: 63px; right: 63px; transform: translateY(-50%); white-space: nowrap; line-height: 1; text-transform: uppercase; }
  .indent { left: 150px; }
  .initial { position: absolute; left: 60px; transform: translateY(-50%); color: var(--mint); -webkit-text-stroke: 2px var(--pine); line-height: 1; }
  .title { top: 74px; font-family: "Graduate", serif; font-size: 50px; text-align: center; color: var(--pine); letter-spacing: 1px; }
  .committed { top: 149px; font-family: "Alfa Slab One", serif; font-size: 34px; letter-spacing: 9px; }
  .compassion { top: 203px; font-family: "Alfa Slab One", serif; font-size: 36px; }
  .care { top: 256px; left: 63px; font-family: "Alfa Slab One", serif; font-size: 23px; color: var(--sage); }
  .means { top: 318px; font-family: "Audiowide", sans-serif; font-size: 35px; letter-spacing: 4px; }
  .always { top: 372px; font-family: "Audiowide", sans-serif; font-size: 37px; letter-spacing: 3px; }
  .resources { top: 423px; font-family: "Almendra", serif; font-weight: 700; font-size: 49px; color: var(--fern); }
  .savings { top: 482px; font-family: "Fondamento", serif; font-size: 38px; }
  .savings .bone { display: inline-block; padding: 4px 22px; border: 3px solid var(--mint); border-radius: 22px; margin-right: 14px; margin-left: -6px; }
  .also { top: 546px; font-family: "Michroma", sans-serif; font-size: 24px; letter-spacing: 14px; }
  .ready { top: 602px; font-family: "Racing Sans One", sans-serif; font-size: 60px; font-style: italic; }
  .medicine { top: 684px; font-family: "Russo One", sans-serif; font-size: 48px; font-style: italic; color: var(--pine); display: flex; justify-content: space-between; align-items: center; }
  .available { top: 741px; font-family: "Exo 2", sans-serif; font-size: 34px; letter-spacing: 15px; font-style: italic; }
  .expanding { top: 792px; font-family: "Exo 2", sans-serif; font-weight: 900; font-style: italic; font-size: 37px; }
  .practice { top: 848px; font-family: "Exo 2", sans-serif; font-weight: 300; font-style: italic; font-size: 36px; }
  .provide { top: 915px; font-family: "Rye", serif; font-size: 38px; }
  .abundance { top: 974px; font-family: "Rye", serif; font-size: 44px; }
  .pair { display: flex; justify-content: space-between; align-items: center; }
  .pair .left { font-family: "Skranji", sans-serif; font-weight: 700; font-style: italic; color: var(--fern); font-size: 31px; }
  .pair .right { font-family: "Bungee Hairline", sans-serif; font-size: 30px; font-weight: 700; color: var(--fern); -webkit-text-stroke: 1px var(--fern); letter-spacing: 2px; }
  .row1 { top: 1036px; }
  .row2 { top: 1088px; }
  .closing { top: 1146px; display: flex; align-items: center; justify-content: space-between; }
  .closing .see { font-family: "Skranji", sans-serif; font-weight: 700; font-size: 30px; color: var(--pine); }
  .closing .signoff { font-family: "Graduate", serif; font-size: 36px; color: var(--pine); }
  .icon { display: inline-block; }
  .art { position: absolute; }
</style>
</head>
<body>
<main class="sign">
  <div class="pattern" role="img" aria-label="Faint line-drawn pattern of cats, dogs and paw prints"></div>

  <h1 class="line title">Pravo Veterinary Services</h1>

  <span class="initial" style="top:176px;font-family:'Alfa Slab One',serif;font-size:112px;">C</span>
  <p class="line indent committed">is committed to</p>
  <div class="art" role="img" aria-label="Small cat face doodle" style="left:800px;top:132px;width:60px;height:34px;background:var(--mint);border-radius:40%;"></div>
  <p class="line indent compassion">ompassionate and honest</p>
  <p class="line care">Care for all patients and clients.</p>
  <div class="art" role="img" aria-label="Paw print with medical cross" style="left:790px;top:225px;width:78px;height:84px;background:var(--sage);border-radius:45%;"></div>

  <span class="initial" style="top:345px;font-family:'Audiowide',sans-serif;font-size:104px;">A</span>
  <p class="line indent means">This means we are</p>
  <p class="line indent always">lways efficient with</p>
  <p class="line resources">Our resources to pass</p>
  <p class="line savings"><span class="bone">The savings</span>on to our clients.</p>

  <span class="initial" style="top:577px;font-family:'Racing Sans One',sans-serif;font-style:italic;font-size:104px;">R</span>
  <p class="line indent also">We are also</p>
  <p class="line indent ready">eady to help with</p>
  <p class="line medicine">
    <span>The best</span>
    <span class="icon" role="img" aria-label="Medical cross with animal silhouettes" style="width:70px;height:74px;background:var(--fern);border-radius:6px;"></span>
    <span>medicine</span>
  </p>

  <span class="initial" style="top:768px;font-family:'Exo 2',sans-serif;font-weight:900;font-size:104px;">E</span>
  <p class="line indent available">available while</p>
  <p class="line indent expanding">xpanding to help more of</p>
  <p class="line practice">Our practice’s families and farms.</p>

  <span class="initial" style="top:944px;font-family:'Rye',serif;font-size:112px;">S</span>
  <p class="line indent provide">This is how we provide</p>
  <p class="line indent abundance">ervice in abundance</p>
  <p class="line pair row1"><span class="left">To all our clients so</span><span class="right">their family</span></p>
  <p class="line pair row2"><span class="left">they are proud to send</span><span class="right">and friends</span></p>
  <p class="line closing">
    <span class="see">To see us.</span>
    <span class="icon" role="img" aria-label="Heart framing a cat, dog and cow" style="width:80px;height:62px;background:var(--pine);border-radius:40% 40% 50% 50%;"></span>
    <span class="signoff">Pravo Vet CARES</span>
  </p>
</main>
</body>
</html>
```